Kerno Solutions: searching for a flyer to trow in letterboxes for properties we are interested in

Hello ,

Introduction:
We are a company based in Luxembourg called "Kerno Solutions". We are specialized in buying properties on which we develop and build constructions before selling them.

Informations for the flyer:
We need a flyer to trow into the letter boxes of property owners letting them know that we are interested in buying their property, if they are interested they can give us a call.

The text for the flyer/letter is in the attachment called >>2020-03-11_KS_Text for flyer,letter there might be slight changes<<.

We need to look competent, professional and financially stable.

The flyer needs to be short and not over welling with information otherwise it will land in the trash.

We have decided that we don't want real pictures on the flyer, but shapes of any kind, blue prints, drawings are fine.

Format should be in DIN A4. We plan to print the flyer on both sides in two different languages, in other words the design will be the same on both sides only the text will be in a different language.

I also added our current logo and here is the design of the website that is under construction at the moment http://www.kernosolutions-example.lu/. The logo's color can be changed into a different blue or uni color (all white or all black).
Updates

Hi, First time user the howl thing started faster as expected. Furthermore, I need to catch my boss to discust the project with him and he is on a lot of meetings. Please give us a little bit more time. Thanks

Target Market(s)

Property owners

Requirements
Must have
• email, phone number, tax number (RCS), Tax number , matriculation and address.
see word file in attachment for information
Nice to have
• Our company logo, in one form or an other, you can be creative, the logo is in the attachment.
Should not have
• Real pictures

```html
<!DOCTYPE html>
<html lang="fr">
<head>
<meta charset="utf-8">
<title>Kerno Solutions – Flyer recto / verso</title>
<link rel="stylesheet" href="https://fonts.googleapis.com/css2?family=Bebas+Neue&family=Source+Sans+3:ital,wght@0,400;0,600;1,700&display=swap">
<style>
  :root{
    --backdrop:#939598;
    --paper:#ffffff;
    --paper-soft:#eef0f2;
    --blue-light:#3aa8e0;
    --blue-mid:#2a86c2;
    --blue-deep:#1b5f95;
    --blue-badge:#2fa3dc;
    --ink:#333538;
    --ink-dark:#2e2f31;
    --grey-shape:#a9adb2;
  }
  *{margin:0;padding:0;box-sizing:border-box}
  html,body{width:1200px;height:842px;overflow:hidden;background:var(--backdrop)}
  .spread{position:relative;width:1200px;height:842px}
  .sheet{
    position:absolute;top:68px;width:595px;height:842px;
    transform:scale(0.822);transform-origin:0 0;
    background:var(--paper);overflow:hidden;
    box-shadow:0 4px 14px rgba(0,0,0,.35);
    font-family:"Source Sans 3",Arial,sans-serif;color:var(--ink);
  }
  .sheet--fr{left:80px}
  .sheet--lb{left:629px}
  .sheet__shapes{position:absolute;inset:0}
  .greeting{
    position:absolute;right:24px;top:28px;
    font-family:"Bebas Neue",Impact,sans-serif;font-size:38px;line-height:1;color:#fff;letter-spacing:.3px;
  }
  .greeting-rule{position:absolute;left:440px;top:83px;width:131px;height:2px;background:#fff}
  .intro{position:absolute;right:24px;width:290px;text-align:right;color:#fff;font-size:13px;line-height:18px}
  .intro--one{top:96px}
  .intro--two{top:150px}
  .body-copy{position:absolute;left:24px;width:340px;font-size:13px;line-height:16px;color:var(--ink)}
  .body-copy--one{top:347px}
  .body-copy--two{top:395px}
  .closing{position:absolute;left:24px;top:459px;font-size:13px}
  .signature{position:absolute;left:24px;top:486px;font-size:14px;font-weight:700;font-style:italic;color:var(--ink)}
  .quote-badge{
    position:absolute;left:381px;top:378px;width:94px;height:94px;border-radius:50%;
    background:var(--blue-badge);border:3px solid #fff;box-shadow:0 2px 6px rgba(0,0,0,.25);
    display:flex;align-items:center;justify-content:center;text-align:center;
    font-family:"Bebas Neue",Impact,sans-serif;font-size:17px;line-height:17px;color:#fff;
  }
  .brand-name{
    position:absolute;left:30px;top:660px;
    font-family:"Bebas Neue",Impact,sans-serif;font-size:29px;line-height:1;color:var(--blue-deep);letter-spacing:.4px;
  }
  .contact-list{position:absolute;left:27px;top:713px;list-style:none}
  .contact-list li{display:flex;align-items:center;height:19.5px;font-size:12.5px;color:var(--ink)}
  .contact-list svg{width:13px;height:13px;margin-right:11px;flex:none}
</style>
</head>
<body>
<main class="spread">

  <!-- French side -->
  <article class="sheet sheet--fr" lang="fr">
    <svg class="sheet__shapes" viewBox="0 0 595 842" width="595" height="842">
      <defs>
        <linearGradient id="fr-blue" x1="0" y1="0" x2="0.5" y2="1">
          <stop offset="0" stop-color="#3aa8e0"/><stop offset="1" stop-color="#1e6aa2"/>
        </linearGradient>
        <linearGradient id="fr-soft" x1="0" y1="0" x2="0" y2="1">
          <stop offset="0" stop-color="#f6f7f8"/><stop offset="1" stop-color="#e7e9eb"/>
        </linearGradient>
        <linearGradient id="fr-house" x1="0" y1="0" x2="1" y2="1">
          <stop offset="0" stop-color="#eceeef"/><stop offset="1" stop-color="#c9ccd0"/>
        </linearGradient>
        <linearGradient id="fr-model" x1="0" y1="0" x2="1" y2="1">
          <stop offset="0" stop-color="#e2c596"/><stop offset="1" stop-color="#a8865b"/>
        </linearGradient>
      </defs>
      <rect x="0" y="280" width="595" height="282" fill="url(#fr-soft)"/>
      <polygon points="0,0 171,0 250,130 200,280 0,280" fill="url(#fr-house)" role="img" aria-label="Maison dessinée sur des plans d'architecte"/>
      <polygon points="172,280 250,158 336,280" fill="var(--grey-shape)"/>
      <polygon points="171,0 595,0 595,562 503,562" fill="url(#fr-blue)"/>
      <polygon points="288,200 370,200 595,575 595,730" fill="#15598c" opacity=".55"/>
      <polygon points="433,562 595,562 595,842 373,842 286,665 343,607" fill="url(#fr-model)" role="img" aria-label="Maquette de maison posée sur un plan avec un crayon"/>
      <polygon points="503,562 595,562 595,720" fill="#1b6aa3" opacity=".85"/>
      <rect x="0" y="817" width="320" height="25" fill="var(--ink-dark)"/>
      <polygon points="315,842 373,782 403,842" fill="var(--blue-deep)"/>
    </svg>

    <h1 class="greeting">Madame, Monsieur,</h1>
    <div class="greeting-rule"></div>
    <p class="intro intro--one">Ce courrier vous a été adressé, car votre propriété a attiré notre attention.</p>
    <p class="intro intro--two">Nous souhaiterions discuter avec vous de son éventuel rachat par notre société.</p>

    <p class="body-copy body-copy--one">En cas d’accord, nous vous assurons une décision rapide, un paiement garanti, et zéro frais d’intermédiaire.</p>
    <p class="body-copy body-copy--two">En attendant de vos nouvelles, nous restons à votre entière disposition pour tout renseignement.</p>
    <p class="closing">Salutations distinguées</p>
    <p class="signature">L’ÉQUIPE DE KERNO SOLUTIONS</p>

    <div class="quote-badge">Call us<br>for a<br>free quote</div>

    <p class="brand-name">Kerno Solutions</p>
    <ul class="contact-list">
      <li><svg viewBox="0 0 13 13"><rect width="13" height="13" rx="2" fill="var(--blue-deep)"/><path d="M4 3l1.5 0 .6 2-1 .8a5 5 0 0 0 2.1 2.1l.8-1 2 .6V9.5A1 1 0 0 1 9 10.5 6.5 6.5 0 0 1 3 4.5 1 1 0 0 1 4 3z" fill="#fff"/></svg>+352 600.100.200 | 352 200.300.40</li>
      <li><svg viewBox="0 0 13 13"><rect width="13" height="13" rx="2" fill="var(--blue-deep)"/><circle cx="6.5" cy="6.5" r="3.8" fill="none" stroke="#fff"/><path d="M2.7 6.5h7.6M6.5 2.7c-2 2.4-2 5.2 0 7.6M6.5 2.7c2 2.4 2 5.2 0 7.6" fill="none" stroke="#fff" stroke-width=".8"/></svg>kernosolutions-example.lu</li>
      <li><svg viewBox="0 0 13 13"><rect width="13" height="13" rx="2" fill="var(--blue-deep)"/><path d="M6.5 2a3 3 0 0 1 3 3c0 2.2-3 6-3 6s-3-3.8-3-6a3 3 0 0 1 3-3z" fill="#fff"/><circle cx="6.5" cy="5" r="1.1" fill="var(--blue-deep)"/></svg>12 rue des Tilleuls, L-0000 Exempleville</li>
      <li><svg viewBox="0 0 13 13"><rect width="13" height="13" rx="2" fill="var(--blue-deep)"/><rect x="2.5" y="3.8" width="8" height="5.6" fill="none" stroke="#fff"/><path d="M2.5 3.8l4 3.2 4-3.2" fill="none" stroke="#fff"/></svg>info@kernosolutions-example.lu</li>
    </ul>
  </article>

  <!-- Luxembourgish side -->
  <article class="sheet sheet--lb" lang="lb">
    <svg class="sheet__shapes" viewBox="0 0 595 842" width="595" height="842">
      <defs>
        <linearGradient id="lb-blue" x1="0" y1="0" x2="0.5" y2="1">
          <stop offset="0" stop-color="#3aa8e0"/><stop offset="1" stop-color="#1e6aa2"/>
        </linearGradient>
        <linearGradient id="lb-soft" x1="0" y1="0" x2="0" y2="1">
          <stop offset="0" stop-color="#f6f7f8"/><stop offset="1" stop-color="#e7e9eb"/>
        </linearGradient>
        <linearGradient id="lb-house" x1="0" y1="0" x2="1" y2="1">
          <stop offset="0" stop-color="#eceeef"/><stop offset="1" stop-color="#c9ccd0"/>
        </linearGradient>
        <linearGradient id="lb-model" x1="0" y1="0" x2="1" y2="1">
          <stop offset="0" stop-color="#e2c596"/><stop offset="1" stop-color="#a8865b"/>
        </linearGradient>
      </defs>
      <rect x="0" y="280" width="595" height="282" fill="url(#lb-soft)"/>
      <polygon points="0,0 171,0 250,130 200,280 0,280" fill="url(#lb-house)" role="img" aria-label="Haus op Architektepläng gezeechent"/>
      <polygon points="172,280 250,158 336,280" fill="var(--grey-shape)"/>
      <polygon points="171,0 595,0 595,562 503,562" fill="url(#lb-blue)"/>
      <polygon points="288,200 370,200 595,575 595,730" fill="#15598c" opacity=".55"/>
      <polygon points="433,562 595,562 595,842 373,842 286,665 343,607" fill="url(#lb-model)" role="img" aria-label="Hausmodell op engem Plang mat engem Bläistëft"/>
      <polygon points="503,562 595,562 595,720" fill="#1b6aa3" opacity=".85"/>
      <rect x="0" y="817" width="320" height="25" fill="var(--ink-dark)"/>
      <polygon points="315,842 373,782 403,842" fill="var(--blue-deep)"/>
    </svg>

    <h1 class="greeting">Madame, Monsieur,</h1>
    <div class="greeting-rule"></div>
    <p class="intro intro--one">Dir kritt dëst Schreiwes well Är Proprietéit eis Opmierksamkeet zeréckbehalen huet.</p>
    <p class="intro intro--two">Mir géinge gär mat Iech iwwert d’Méiglechkeet, datt eise Betrib se opkeeft, diskutéieren.</p>

    <p class="body-copy body-copy--one">Mir verséchere Iech e séieren Entscheedungsprozess, garantéieren d’Bezuelung a verrechne keng Drëttkäschten.</p>
    <p class="body-copy body-copy--two" style="top:411px">Mir géingen eis freeën, vun Iech ze héieren, a sti ganz zu Ärer Verfügung fir zousätzlech Informatiounen.</p>
    <p class="closing" style="top:475px">Mat beschte Gréiss,</p>
    <p class="signature" style="top:497px">D’EQUIPE VUN KERNO SOLUTIONS</p>

    <div class="quote-badge">Call us<br>for a<br>free quote</div>

    <p class="brand-name">Kerno Solutions</p>
    <ul class="contact-list">
      <li><svg viewBox="0 0 13 13"><rect width="13" height="13" rx="2" fill="var(--blue-deep)"/><path d="M4 3l1.5 0 .6 2-1 .8a5 5 0 0 0 2.1 2.1l.8-1 2 .6V9.5A1 1 0 0 1 9 10.5 6.5 6.5 0 0 1 3 4.5 1 1 0 0 1 4 3z" fill="#fff"/></svg>+352 600.100.200 | 352 200.300.40</li>
      <li><svg viewBox="0 0 13 13"><rect width="13" height="13" rx="2" fill="var(--blue-deep)"/><circle cx="6.5" cy="6.5" r="3.8" fill="none" stroke="#fff"/><path d="M2.7 6.5h7.6M6.5 2.7c-2 2.4-2 5.2 0 7.6M6.5 2.7c2 2.4 2 5.2 0 7.6" fill="none" stroke="#fff" stroke-width=".8"/></svg>kernosolutions-example.lu</li>
      <li><svg viewBox="0 0 13 13"><rect width="13" height="13" rx="2" fill="var(--blue-deep)"/><path d="M6.5 2a3 3 0 0 1 3 3c0 2.2-3 6-3 6s-3-3.8-3-6a3 3 0 0 1 3-3z" fill="#fff"/><circle cx="6.5" cy="5" r="1.1" fill="var(--blue-deep)"/></svg>12 rue des Tilleuls, L-0000 Exempleville</li>
      <li><svg viewBox="0 0 13 13"><rect width="13" height="13" rx="2" fill="var(--blue-deep)"/><rect x="2.5" y="3.8" width="8" height="5.6" fill="none" stroke="#fff"/><path d="M2.5 3.8l4 3.2 4-3.2" fill="none" stroke="#fff"/></svg>info@kernosolutions-example.lu</li>
    </ul>
  </article>

</main>
</body>
</html>
```